Silver cove Convenience store

I have just purchased a business you can see picture its very dated. It needs a fresh feel on top to say silver cove Convenience store.
Underneath it could say something like groceries, fruit vegies and more. On the window it would be beter left clean on the top but at the bottom maybee pictures of fresh fruits vegetables and general items a high end gourmet feel
Updates
The photograph i have sent is the shop i purchased, and the old signage. Its very outdated i need it to be very clear and in date Added Wednesday, October 12, 2016
Im looking for it to have a more gourmet or high end feel Added Friday, October 14, 2016

```html
<!DOCTYPE html>
<html lang="en">
<head>
<meta charset="utf-8">
<title>Silver Cove Convenience Store – Shopfront Signage</title>
<link rel="stylesheet" href="https://fonts.googleapis.com/css2?family=Yesteryear&family=Dancing+Script:wght@500&display=swap">
<style>
  :root {
    --bg: #ecebe7;
    --sign-cream: #f4ebc8;
    --ink: #111111;
    --frame: #050505;
    --glass-top: #9c9c9c;
    --glass-mid: #e6e6e6;
    --sand: #ddd3be;
    --sand-dark: #cbbfa5;
    --illus: #b9d9ea;
    --white: #ffffff;
  }
  * { margin: 0; padding: 0; box-sizing: border-box; }
  html, body { width: 1200px; height: 675px; overflow: hidden; background: var(--bg); }
  .canvas { position: relative; width: 1200px; height: 675px; }

  .fascia {
    position: absolute; left: 10px; top: 70px; width: 1160px; height: 156px;
    background: var(--sign-cream);
    box-shadow: 0 2px 0 rgba(0,0,0,.12);
  }
  .rule { position: absolute; left: 22px; right: 22px; height: 2px; background: var(--ink); }
  .fascia .rule.top { top: 14px; }
  .fascia .rule.bottom { bottom: 14px; }
  .fascia-title {
    position: absolute; inset: 0; display: flex; align-items: center; justify-content: center;
    font-family: "Yesteryear", cursive; font-weight: 400; font-size: 74px; line-height: 1;
    color: var(--ink); word-spacing: 12px; white-space: nowrap;
  }

  .subsign {
    position: absolute; left: 193px; top: 253px; width: 752px; height: 72px;
    background: var(--sign-cream);
  }
  .subsign .rule { left: 12px; right: 12px; height: 1.5px; }
  .subsign .rule.top { top: 8px; }
  .subsign .rule.bottom { bottom: 6px; }
  .subsign-text {
    position: absolute; inset: 0; display: flex; align-items: center; justify-content: center;
    font-family: "Yesteryear", cursive; font-size: 33px; line-height: 1; color: var(--ink);
    word-spacing: 5px; white-space: nowrap;
  }

  .window-frame {
    position: absolute; left: 193px; top: 325px; width: 754px; height: 235px;
    background: var(--frame);
  }
  .pane {
    position: absolute; top: 5px; height: 228px;
    background: linear-gradient(180deg, var(--glass-top) 0%, var(--glass-mid) 40%, var(--white) 50%, var(--sand) 50.2%, var(--sand-dark) 100%);
  }
  .pane.p1 { left: 25px; width: 166px; }
  .pane.p2 { left: 194px; width: 156px; }
  .pane.p3 { left: 353px; width: 24px; }
  .pane.p4 { left: 401px; width: 150px; }
  .pane.p5 { left: 554px; width: 148px; }
  .pane.p6 { left: 705px; width: 28px; }

  .label {
    position: absolute; font-family: "Dancing Script", cursive; font-size: 9px; line-height: 1;
    color: var(--ink); white-space: nowrap;
  }
  .artwork { position: absolute; background: var(--illus); border-radius: 6px; opacity: .85; }

  .bubble { position: absolute; }
  .bubble-text {
    position: absolute; inset: 0; display: flex; flex-direction: column; align-items: center; justify-content: center;
    font-family: "Dancing Script", cursive; color: var(--white); line-height: 1.1; text-align: center; white-space: nowrap;
  }
</style>
</head>
<body>
<main class="canvas">

  <header class="fascia">
    <div class="rule top"></div>
    <div class="rule bottom"></div>
    <h1 class="fascia-title">Silver Cove Convenience Store</h1>
  </header>

  <section class="subsign">
    <div class="rule top"></div>
    <div class="rule bottom"></div>
    <p class="subsign-text">Groceries, fruits, vegetables and more!</p>
  </section>

  <section class="window-frame">
    <div class="pane p1">
      <span class="label" style="left:60px; top:118px;">"Fresh Fruits &amp; Vegetables"</span>
      <div class="artwork" style="left:12px; top:132px; width:146px; height:90px;" role="img" aria-label="Line illustration of fresh vegetables and fruit"></div>
    </div>
    <div class="pane p2">
      <svg class="bubble" style="left:108px; top:84px;" width="44" height="28" viewBox="0 0 44 28" aria-hidden="true">
        <ellipse cx="22" cy="12" rx="21" ry="11" fill="var(--ink)"/>
        <path d="M25 21 L31 28 L30 20 Z" fill="var(--ink)"/>
      </svg>
      <div class="bubble" style="left:108px; top:84px; width:44px; height:24px;">
        <div class="bubble-text" style="font-size:7px;">Slide Open
          <svg width="22" height="5" viewBox="0 0 22 5" aria-hidden="true"><path d="M21 2.5 H2 M5 0.5 L1.5 2.5 L5 4.5" stroke="var(--white)" stroke-width="0.9" fill="none"/></svg>
        </div>
      </div>
    </div>
    <div class="pane p3"></div>
    <div class="pane p4">
      <svg class="bubble" style="left:38px; top:38px;" width="78" height="52" viewBox="0 0 78 52" aria-hidden="true">
        <ellipse cx="39" cy="21" rx="38" ry="20" fill="var(--ink)"/>
        <path d="M32 38 L32 52 L44 40 Z" fill="var(--ink)"/>
      </svg>
      <div class="bubble" style="left:38px; top:38px; width:78px; height:42px;">
        <div class="bubble-text" style="font-size:10px;"><span>Open Daily</span><span>7am - 7pm</span></div>
      </div>
      <span class="label" style="left:50px; top:123px;">"Fresh Juices"</span>
      <div class="artwork" style="left:28px; top:134px; width:24px; height:44px;" role="img" aria-label="Line illustration of a juice bottle"></div>
      <span class="label" style="left:80px; top:150px;">"Dairy Products"</span>
      <div class="artwork" style="left:90px; top:172px; width:30px; height:44px;" role="img" aria-label="Line illustration of a milk carton"></div>
    </div>
    <div class="pane p5">
      <span class="label" style="left:20px; top:123px;">"Breads &amp; Pastries"</span>
      <div class="artwork" style="left:56px; top:144px; width:84px; height:64px;" role="img" aria-label="Line illustration of a bread loaf, baguette and pastries"></div>
    </div>
    <div class="pane p6"></div>
  </section>

</main>
</body>
</html>
```